Power Point for a new training package

I am a new business and about to offer my first teaching day. I have all the content, have a logo etc. but need to translate this into a slick bespoke Power Point presentation,

Target Market(s)

Senior people in healthcare sector, UK

Industry/Entity Type

Healthcare

Requirements
Must have
• Sense of originality, use of my logo and associated colour scheme, stylish but simple

```html
<!DOCTYPE html>
<html lang="en">
<head>
<meta charset="utf-8">
<title>Training Day Presentation – Slide Overview</title>
<link href="https://fonts.googleapis.com/css2?family=Inter+Tight:wght@400;500;600&display=swap" rel="stylesheet">
<style>
  :root{
    --teal:#22b2ad;
    --teal-bright:#5fe0de;
    --teal-soft:#a9e7e4;
    --teal-wash:#e9fbfb;
    --mist:#e5e9ee;
    --ink:#141414;
    --white:#ffffff;
    --font:"Inter Tight", "Helvetica Neue", Arial, sans-serif;
  }
  *{box-sizing:border-box;margin:0;padding:0}
  html,body{width:1200px;height:849px;overflow:hidden}
  body{background:var(--white);font-family:var(--font);color:var(--ink);position:relative}

  .slide{position:absolute;width:372px;height:210px;overflow:hidden;background:var(--white);
    box-shadow:0 6px 18px rgba(0,0,0,.12)}
  .col-1{left:30px}.col-2{left:419px}.col-3{left:808px}
  .row-1{top:97px}.row-2{top:320px}.row-3{top:542px}

  .heading{font-weight:500;letter-spacing:-.06em;line-height:.98}
  .body-copy{font-size:5.3px;line-height:1.6;font-weight:500}
  .micro{font-size:3.4px;line-height:1.55;font-weight:500}

  /* brand mark */
  .brand{display:flex;flex-direction:column;align-items:center;gap:2px;position:absolute}
  .brand-dot{width:10px;height:10px;border-radius:50%;border:1.2px solid var(--teal)}
  .brand-name{font-size:4.4px;font-weight:600;text-align:center;line-height:1.15;color:var(--ink)}
  .corner-tab{position:absolute;right:0;top:0;width:41px;height:40px;background:var(--white);
    border-bottom-left-radius:22px}
  .corner-tab .brand{left:6px;top:7px;width:32px}
  .corner-tab .brand-dot{width:8px;height:8px}
  .corner-tab .brand-name{font-size:3.1px}

  .art{position:absolute}

  /* 1 – title */
  .title-slide .brand{left:22px;top:18px}
  .title-slide .brand-name{font-size:5px}
  .title-slide .heading{position:absolute;left:20px;top:69px;font-size:22.5px}
  .title-slide .subtitle{position:absolute;left:20px;top:118px;font-size:11px;color:var(--teal);letter-spacing:-.05em}
  .web{position:absolute;font-size:7.4px;color:var(--teal);letter-spacing:-.03em;font-weight:500}
  .title-slide .web{left:20px;top:181px}
  .title-slide .art{left:186px;top:6px;width:180px;height:197px;
    background:linear-gradient(160deg,#ececec,#e2e2e2)}
  .title-slide .art::after{content:"";position:absolute;left:22px;top:36px;width:136px;height:126px;
    background:linear-gradient(135deg,#9fd4da,#f4eadf 55%,#7fa6cf)}

  /* 2 – introduction */
  .intro-slide{background:var(--teal)}
  .intro-slide .heading{position:absolute;left:25px;top:51px;font-size:19.5px}
  .intro-slide .body-copy{position:absolute;left:25px;top:113px;width:162px;color:var(--white)}
  .intro-slide .art{left:204px;top:38px;width:150px;height:136px}

  /* 3 – team */
  .team-slide{background:var(--mist)}
  .team-slide .heading{position:absolute;left:0;right:0;top:18px;text-align:center;font-size:19.5px;color:var(--teal)}
  .team-card{position:absolute;top:76px;width:90px;height:113px;background:var(--white);border-radius:5px;padding:0 5px}
  .team-card .portrait{height:79px;margin:0 2px;background:linear-gradient(180deg,#eef1f4,#c9d4de)}
  .team-card .micro{margin-top:6px}

  /* 4 – style 1 */
  .style-one .heading{position:absolute;left:24px;top:64px;font-size:19.5px}
  .style-one .body-copy{position:absolute;left:24px;top:99px;width:162px}
  .step{position:absolute;left:196px;width:145px;height:49px;background:var(--teal);
    border-radius:3px;box-shadow:0 1px 2px rgba(0,0,0,.3);display:flex;align-items:center;gap:10px;padding:0 11px}
  .step-num{font-size:23px;font-weight:500;letter-spacing:-.08em;color:var(--white);width:27px}
  .step .micro{color:var(--white);width:80px}

  /* 5 – style 2 */
  .style-two{background:var(--teal-wash)}
  .style-two .heading{position:absolute;left:25px;top:64px;font-size:19.5px}
  .style-two .body-copy{position:absolute;left:25px;top:99px;width:162px}
  .style-two .art{left:208px;top:44px;width:144px;height:120px;border-radius:6px;
    background:linear-gradient(135deg,#cfe4ea,#ffffff 45%,#2fb6b0)}

  /* 6 – programs */
  .programs-slide .heading{position:absolute;left:0;right:0;top:35px;text-align:center;font-size:18.5px}
  .program{position:absolute;top:83px;width:108px;height:98px;text-align:center;padding:10px 9px 0}
  .program .step-num{width:auto;color:var(--ink);font-size:23px;display:block;margin-bottom:6px}
  .program .micro{font-size:3.6px}
  .p1{left:21px;background:var(--teal)}
  .p2{left:133px;background:var(--teal-bright)}
  .p3{left:245px;background:var(--teal-soft)}

  /* 7 – stat */
  .stat-slide{background:var(--teal);color:var(--white);text-align:center}
  .stat-slide .stat{position:absolute;left:0;right:0;top:37px;font-size:46px;font-weight:400;letter-spacing:-.06em;line-height:1}
  .stat-slide .heading{position:absolute;left:0;right:0;top:89px;font-size:13px}
  .stat-slide .body-copy{position:absolute;left:68px;right:68px;top:127px;color:var(--ink)}

  /* 8 – conclusion */
  .conclusion-slide{background:var(--teal);padding:7px}
  .conclusion-panel{position:relative;width:100%;height:100%;background:var(--white);text-align:center}
  .conclusion-panel .brand{left:0;right:0;top:15px}
  .conclusion-panel .heading{position:absolute;left:0;right:0;top:51px;font-size:18.5px;color:var(--teal)}
  .conclusion-panel .body-copy{position:absolute;left:70px;right:70px;top:100px}

  /* 9 – thanks */
  .thanks-slide .brand{left:23px;top:18px}
  .thanks-slide .heading{position:absolute;left:21px;top:51px;font-size:36px;color:var(--teal);letter-spacing:-.07em;line-height:1}
  .thanks-slide .web{left:21px;top:183px}
  .thanks-slide .art{left:187px;top:6px;width:181px;height:198px;background:var(--teal-wash)}
  .thanks-slide .art::after{content:"";position:absolute;left:20px;top:36px;width:140px;height:128px;
    background:linear-gradient(135deg,#f7ece6,#ffffff 40%,#2fb6b0)}
</style>
</head>
<body>

<!-- 1 -->
<section class="slide col-1 row-1 title-slide">
  <div class="brand"><span class="brand-dot"></span><span class="brand-name">Marlow Hale<br>Consulting</span></div>
  <h1 class="heading">Your presentation<br>title here</h1>
  <p class="subtitle">Subtitle goes here</p>
  <p class="web">www.website.com</p>
  <div class="art" role="img" aria-label="Illustration of a patient and a doctor shaking hands between two phone screens"></div>
</section>

<!-- 2 -->
<section class="slide col-2 row-1 intro-slide">
  <div class="corner-tab"><div class="brand"><span class="brand-dot"></span><span class="brand-name">Marlow Hale<br>Consulting</span></div></div>
  <h2 class="heading">Introduction:<br>Presentation<br>introduction here.</h2>
  <p class="body-copy">Lorem ipsum dolor sit amet, consectetur adipiscing elit, sed do eiusmod tempor incididunt ut labore et dolore magna aliqua. Ut enim ad minim veniam, quis nostrud exercitation ullamco laboris nisi ut aliquip ex ea commodo consequat. Duis aute irure dolor in reprehenderit in voluptate velit esse cillum dolore eu fugiat nulla pariatur.</p>
  <svg class="art" viewBox="0 0 150 136" role="img" aria-label="Photograph of a doctor meeting patients, cropped in a rounded blob shape">
    <defs><linearGradient id="blobFill" x1="0" y1="0" x2="1" y2="1"><stop offset="0" stop-color="#f1efec"/><stop offset=".55" stop-color="#c9c3bf"/><stop offset="1" stop-color="#8fa3b5"/></linearGradient></defs>
    <path d="M12 34C22 8 48 0 70 6c18 5 32 10 50 4 20-6 30 10 30 34 0 34-6 66-22 84-14 16-40 8-60-6C44 108 20 96 6 74-2 60 4 48 12 34Z" fill="url(#blobFill)"/>
  </svg>
</section>

<!-- 3 -->
<section class="slide col-3 row-1 team-slide">
  <div class="corner-tab"><div class="brand"><span class="brand-dot"></span><span class="brand-name">Marlow Hale<br>Consulting</span></div></div>
  <h2 class="heading">Our medical team:<br>Dedicated professionals</h2>
  <article class="team-card" style="left:43px">
    <div class="portrait" role="img" aria-label="Portrait photo of a doctor in a white coat"></div>
    <p class="micro">Lorem ipsum dolor sit amet, consectetur adipiscing elit, sed do eiusmod tempor incididunt ut labore et dolore magna aliqua. Ut enim ad minim veniam.</p>
  </article>
  <article class="team-card" style="left:141px">
    <div class="portrait" role="img" aria-label="Portrait photo of a surgeon in blue scrubs"></div>
    <p class="micro">Lorem ipsum dolor sit amet, consectetur adipiscing elit, sed do eiusmod tempor incididunt ut labore et dolore magna aliqua. Ut enim ad minim veniam.</p>
  </article>
  <article class="team-card" style="left:240px">
    <div class="portrait" role="img" aria-label="Portrait photo of a doctor with glasses and a stethoscope"></div>
    <p class="micro">Lorem ipsum dolor sit amet, consectetur adipiscing elit, sed do eiusmod tempor incididunt ut labore et dolore magna aliqua. Ut enim ad minim veniam.</p>
  </article>
</section>

<!-- 4 -->
<section class="slide col-1 row-2 style-one">
  <div class="corner-tab"><div class="brand"><span class="brand-dot"></span><span class="brand-name">Marlow Hale<br>Consulting</span></div></div>
  <h2 class="heading">Sample page style 1</h2>
  <p class="body-copy">Lorem ipsum dolor sit amet, consectetur adipiscing elit, sed do eiusmod tempor incididunt ut labore et dolore magna aliqua. Ut enim ad minim veniam, quis nostrud exercitation ullamco laboris nisi ut aliquip ex ea commodo consequat. Duis aute irure dolor in reprehenderit in voluptate velit esse cillum dolore eu fugiat nulla pariatur.</p>
  <div class="step" style="top:40px"><span class="step-num">01.</span><p class="micro">Lorem ipsum dolor sit amet, consectetur adipiscing elit, sed do eiusmod tempor incididunt ut labore et dolore magna aliqua. Ut enim ad minim veniam, quis nostrud exercitation ullamco laboris nisi ut aliquip ex ea commodo consequat.</p></div>
  <div class="step" style="top:92px"><span class="step-num">02.</span><p class="micro">Lorem ipsum dolor sit amet, consectetur adipiscing elit, sed do eiusmod tempor incididunt ut labore et dolore magna aliqua. Ut enim ad minim veniam, quis nostrud exercitation ullamco laboris nisi ut aliquip ex ea commodo consequat.</p></div>
  <div class="step" style="top:145px"><span class="step-num">03.</span><p class="micro">Lorem ipsum dolor sit amet, consectetur adipiscing elit, sed do eiusmod tempor incididunt ut labore et dolore magna aliqua. Ut enim ad minim veniam, quis nostrud exercitation ullamco laboris nisi ut aliquip ex ea commodo consequat.</p></div>
</section>

<!-- 5 -->
<section class="slide col-2 row-2 style-two">
  <div class="corner-tab"><div class="brand"><span class="brand-dot"></span><span class="brand-name">Marlow Hale<br>Consulting</span></div></div>
  <h2 class="heading">Sample page style 2</h2>
  <p class="body-copy">Lorem ipsum dolor sit amet, consectetur adipiscing elit, sed do eiusmod tempor incididunt ut labore et dolore magna aliqua. Ut enim ad minim veniam, quis nostrud exercitation ullamco laboris nisi ut aliquip ex ea commodo consequat. Duis aute irure dolor in reprehenderit in voluptate velit esse cillum dolore eu fugiat nulla pariatur.</p>
  <div class="art" role="img" aria-label="Illustration of a patient at a laptop consulting a doctor on screen, with scan cards below"></div>
</section>

<!-- 6 -->
<section class="slide col-3 row-2 programs-slide">
  <div class="corner-tab"><div class="brand"><span class="brand-dot"></span><span class="brand-name">Marlow Hale<br>Consulting</span></div></div>
  <h2 class="heading">Health programs:<br>Slide title here</h2>
  <div class="program p1"><span class="step-num">01.</span><p class="micro">Lorem ipsum dolor sit amet, consectetur adipiscing elit, sed do eiusmod tempor incididunt ut labore et dolore magna aliqua. Ut enim ad minim veniam, quis nostrud exercitation ullamco laboris nisi ut aliquip ex ea commodo consequat.</p></div>
  <div class="program p2"><span class="step-num">02.</span><p class="micro">Lorem ipsum dolor sit amet, consectetur adipiscing elit, sed do eiusmod tempor incididunt ut labore et dolore magna aliqua. Ut enim ad minim veniam, quis nostrud exercitation ullamco laboris nisi ut aliquip ex ea commodo consequat.</p></div>
  <div class="program p3"><span class="step-num">03.</span><p class="micro">Lorem ipsum dolor sit amet, consectetur adipiscing elit, sed do eiusmod tempor incididunt ut labore et dolore magna aliqua. Ut enim ad minim veniam, quis nostrud exercitation ullamco laboris nisi ut aliquip ex ea commodo consequat.</p></div>
</section>

<!-- 7 -->
<section class="slide col-1 row-3 stat-slide">
  <div class="corner-tab"><div class="brand"><span class="brand-dot"></span><span class="brand-name">Marlow Hale<br>Consulting</span></div></div>
  <p class="stat">95%</p>
  <h2 class="heading">Success stories: Real stories,<br>tangible results</h2>
  <p class="body-copy">Lorem ipsum dolor sit amet, consectetur adipiscing elit, sed do eiusmod tempor incididunt ut labore et dolore magna aliqua.<br>Ut enim ad minim veniam, quis nostrud exercitation ullamco laboris nisi ut aliquip ex ea commodo consequat. Duis aute irure dolor in reprehenderit in voluptate velit esse cillum dolore eu fugiat nulla pariatur. Excepteur sint occaecat cupidatat non proident, sunt in culpa qui officia deserunt mollit anim id est laborum.</p>
</section>

<!-- 8 -->
<section class="slide col-2 row-3 conclusion-slide">
  <div class="conclusion-panel">
    <div class="brand"><span class="brand-dot"></span><span class="brand-name">Marlow Hale<br>Consulting</span></div>
    <h2 class="heading">Conclusion: Your health,<br>always our priority</h2>
    <p class="body-copy">Lorem ipsum dolor sit amet, consectetur adipiscing elit, sed do eiusmod tempor incididunt ut labore et dolore magna aliqua. Ut enim ad minim veniam, quis nostrud exercitation ullamco laboris nisi ut aliquip ex ea commodo consequat. Duis aute irure dolor in reprehenderit in voluptate velit esse cillum dolore eu fugiat nulla pariatur. Excepteur sint occaecat cupidatat non proident, sunt in culpa qui officia deserunt mollit anim id est laborum.</p>
  </div>
</section>

<!-- 9 -->
<section class="slide col-3 row-3 thanks-slide">
  <div class="brand"><span class="brand-dot"></span><span class="brand-name">Marlow Hale<br>Consulting</span></div>
  <h2 class="heading">Thank<br>you very<br>much!</h2>
  <p class="web">www.website.com</p>
  <div class="art" role="img" aria-label="Illustration of a doctor holding a tablet beside a patient on a video call screen"></div>
</section>

</body>
</html>
```